Homepage für Unternehmensberatung
Zielgruppe
Wir sind eine Unternehmensberatung mit einem klaren Branchenfokus auf Banken / Finanzdienstleister.
Unsere Dienstleistungsprodukte lassen sich grob in folgende Themencluster unterteilen:
1)Strategieentwicklung
o IT-Strategie, IT-Architektur, IT-Bebauungsplan
2) Projektmanagement
o Projektportfoliomgmt., Programmmgmt., Projektmanagement, Projektcontrolling
3) Fachberatung
o Bankfachliche IT- Beratung mit Schwerpunkten Kredit, Wertpapiergeschäft,
Bankenaufsichtsrecht, Liquiditätsmanagement
o Anforderungsmanagement inkl. Aufbau von Bewertungs- und Priorisierungsmethoden
4) Prozessberatung/-optimierung
o Prozessanalyse, Prozessdesign, Prozessdokumentation
o Prozessoptimierung auf Basis etablierter Messmethoden
Unser Firmenname Lotsenwerk hat für uns eine Doppelbedeutung:
1. Im Außenverhältnis: Wir verstehen uns als Lotsenwerk unserer Kunden
2. Im Innenverhältnis: Wir pflegen einen partnerschaftlichen Umgang mit unseren
Mitarbeitern (Teamarbeit)
Aktuell sind wir ein kleines aber feines Team von erfahrenen und hochmotivierten Kollegen. Unsere Mitarbeiter sind ehemalige Führungskräfte sowie erfahrenen Unternehmensberater.
Aufgabenstellung
Entwurf / Design von 2 Seiten:
1. Seite / Startseite:
Simple und elegante Darstellung der oben genannten 4 Themencluster (z.B. Bild/Piktogramm, Textkasten) sowie einer Navigationsmöglichkeit zu folgenden Detailsichten:
• Unternehmen
• Beratungsangebot (siehe Themencluster)
• Partnerunternehmen
• Kontakt
2. Seite / 2. Ebene:
Entwurf einer Möglichkeit zur Erläuterung/Darstellung von Inhalten der Startseite.
Die Themencluster sollten auf jeder Ebene immer „anklickbar“/ zu sehen sein.
Logo
Das angehängte Logo ist in die Website einzubinden. Stil und Farben sollen übernommen werden bzw. sind Basis für das Design.
Lizenzen
Lizenz für eingesetzte Fotos und Illustrationen soll enthalten / Open-Source sein. Wenn nicht dann bitte zusätzliche Kosten angeben.

```html
<!DOCTYPE html>
<html lang="en">
<head>
<meta charset="utf-8">
<title>Lotsenwerk – Management- und Prozessberatung</title>
<link href="https://fonts.googleapis.com/css2?family=Open+Sans:ital,wght@0,400;0,600;0,700;1,700&family=Roboto+Condensed:wght@700&display=swap" rel="stylesheet">
<style>
  :root{
    --page-bg:#5f6870;
    --brand-blue:#1a7fc1;
    --brand-blue-light:#2a9ae0;
    --brand-blue-dark:#11659f;
    --slate:#5d6670;
    --slate-dark:#4d5258;
    --text:#5a6068;
    --white:#ffffff;
    --divider:#9aa0a6;
  }
  *{margin:0;padding:0;box-sizing:border-box}
  html,body{width:1120px;height:1200px;overflow:hidden;background:var(--page-bg)}
  body{position:relative;font-family:"Open Sans",Arial,sans-serif;color:var(--text)}
  .abs{position:absolute}

  /* header */
  .logo-box{left:182px;top:14px;width:274px;height:76px;background:var(--white);border-top:4px solid var(--brand-blue);display:flex;align-items:center;padding-left:14px;gap:10px;z-index:5}
  .logo-dot{width:48px;height:48px;border-radius:50%;background:var(--brand-blue);flex:none}
  .logo-name{font-size:21px;font-weight:400;color:var(--brand-blue);letter-spacing:.5px;line-height:1}
  .logo-tag{font-size:6.5px;color:#8a9096;letter-spacing:1.3px;margin-top:4px;white-space:nowrap}
  .top-contact{top:22px;font-size:12.5px;color:#e6e8ea;display:flex;align-items:center;gap:6px}
  .main-nav{left:168px;top:46px;width:786px;height:44px;background:var(--brand-blue)}
  .main-nav a{position:absolute;top:14px;font-size:12px;font-weight:700;color:var(--white);text-decoration:none;text-transform:uppercase}

  /* hero */
  .hero-photo{left:168px;top:90px;width:786px;height:387px;
    background:linear-gradient(100deg,#7ea2bf 0%,#9db8cf 30%,#c9d6e0 55%,#2b3a55 78%,#d8dde3 100%)}
  .slider-arrow{width:38px;height:50px;background:#4b545c;display:flex;align-items:center;justify-content:center}
  .service-panel{left:237px;top:216px;width:280px;height:240px;border:1px solid rgba(40,50,60,.6);background:rgba(30,40,55,.25)}
  .service-btn{left:244px;width:265px;background:linear-gradient(#2ba0e6,#1673b5);display:flex;align-items:center;color:var(--white);
    font-family:"Roboto Condensed",Arial,sans-serif;font-weight:700;font-size:14.5px;line-height:1.3;text-transform:uppercase;letter-spacing:.3px}
  .service-btn svg{width:30px;height:30px;margin:0 24px 0 8px;flex:none}
  .hero-caption{left:565px;top:352px;width:389px;height:55px;background:rgba(82,88,94,.9);color:var(--white);font-size:18px;display:flex;align-items:center;padding-left:13px}

  /* what we do */
  .wwd-band{left:168px;top:478px;width:786px;height:103px;background:linear-gradient(#1a84c8,#0f6199)}
  .wwd-title{left:168px;width:786px;top:488px;text-align:center;font-family:"Roboto Condensed",Arial,sans-serif;font-weight:700;font-size:32px;color:var(--white)}
  .wwd-body{left:168px;top:581px;width:786px;height:297px;background:var(--white)}
  .cluster-icon{width:86px;height:86px;border-radius:50%;background:var(--white);display:flex;align-items:center;justify-content:center;top:537px}
  .cluster-icon span{width:68px;height:68px;border-radius:50%;background:var(--slate);display:flex;align-items:center;justify-content:center}
  .cluster-title{top:632px;width:196px;text-align:center;font-family:"Roboto Condensed",Arial,sans-serif;font-weight:700;font-size:17.5px;line-height:20px;color:var(--slate);text-transform:uppercase}
  .cluster-list{top:694px;list-style:none;font-size:11.8px;line-height:17.5px;color:var(--text)}
  .cluster-list li{position:relative;padding-left:11px;margin-bottom:7px}
  .cluster-list li::before{content:"";position:absolute;left:0;top:6px;width:4px;height:4px;background:var(--slate)}
  .col-divider{top:605px;height:257px;border-left:1px dotted var(--divider)}

  /* about */
  .about{left:168px;top:878px;width:786px;height:185px;background:linear-gradient(#e6e7e8,#ffffff 70%)}
  .section-title{font-family:"Roboto Condensed",Arial,sans-serif;font-weight:700;font-size:24px;color:var(--slate)}
  .about-text{left:190px;top:929px;width:458px}
  .about-text p{font-size:11.6px;line-height:17.6px;color:var(--text)}
  .v-divider{left:658px;top:897px;height:132px;border-left:1px solid #d3d6d9}
  .quote-mark{font-family:Georgia,serif;font-size:40px;color:#c9cdd1;line-height:1}
  .testimonial{font-size:11.5px;line-height:17.6px;text-align:justify;text-indent:34px}
  .testimonial cite{display:block;font-weight:700;font-style:italic;color:var(--slate);text-indent:0;text-align:left}

  /* footer */
  .site-footer{left:168px;top:1063px;width:786px;height:63px;background:var(--slate-dark)}
  .footer-logo{left:182px;top:1080px;display:flex;align-items:center;gap:6px;color:#7b8188;font-size:13px}
  .footer-logo i{width:28px;height:28px;border-radius:50%;background:#3f4348;display:block}
  .footer-nav{top:1078px;font-size:9.5px;font-weight:600;color:#cfd3d7;text-transform:uppercase}
  .copyright{left:168px;width:786px;top:1096px;text-align:center;font-size:8.5px;color:#cfd3d7;padding-left:8px}
  .social{top:1080px;width:21px;height:21px;border-radius:50%;background:#5f656b}
</style>
</head>
<body>

<header>
  <div class="abs main-nav">
    <a style="left:308px">Company</a>
    <a style="left:397px">Consulting Service</a>
    <a style="left:554px">Partner Companies</a>
    <a style="left:711px">Contact</a>
  </div>
  <div class="abs logo-box">
    <div class="logo-dot"></div>
    <div>
      <div class="logo-name">LOTSENWERK</div>
      <div class="logo-tag">MANAGEMENT- UND PROZESSBERATUNG</div>
    </div>
  </div>
  <div class="abs top-contact" style="left:638px">
    <svg width="16" height="12" viewBox="0 0 16 12"><path d="M1 4c2-3 12-3 14 0l-3 1-1-2H5L4 5z M3 6h10v6H3z" fill="#2f353a"/></svg>
    555-014-2290
  </div>
  <div class="abs top-contact" style="left:766px">
    <svg width="18" height="11" viewBox="0 0 18 11"><rect width="18" height="11" fill="#2f353a"/><path d="M0 0l9 6 9-6" stroke="#5f6870" fill="none"/></svg>
    info@lotsenwerk-beratung.de
  </div>
</header>

<section>
  <div class="abs hero-photo" role="img" aria-label="Photo of a smiling businesswoman holding folders with colleagues blurred in a bright office behind her"></div>
  <div class="abs slider-arrow" style="left:147px;top:234px"><svg width="14" height="20"><path d="M11 2L3 10l8 8" stroke="#c9ced3" stroke-width="3" fill="none"/></svg></div>
  <div class="abs slider-arrow" style="left:934px;top:234px"><svg width="14" height="20"><path d="M3 2l8 8-8 8" stroke="#c9ced3" stroke-width="3" fill="none"/></svg></div>

  <div class="abs service-panel"></div>
  <div class="abs service-btn" style="top:223px;height:42px">
    <svg viewBox="0 0 30 30"><circle cx="15" cy="15" r="12" stroke="#fff" stroke-width="3" fill="none"/><path d="M9 21l4-10 8-2-4 8z" fill="#fff"/></svg>
    Strategy Development
  </div>
  <div class="abs service-btn" style="top:276px;height:58px">
    <svg viewBox="0 0 30 30"><path d="M6 14a9 9 0 0 1 16-5M24 16a9 9 0 0 1-16 5" stroke="#fff" stroke-width="3" fill="none"/><path d="M19 5l5 4-6 2zM11 25l-5-4 6-2z" fill="#fff"/></svg>
    Process Consulting and<br>Optimization
  </div>
  <div class="abs service-btn" style="top:343px;height:42px">
    <svg viewBox="0 0 30 30"><rect x="12" y="4" width="7" height="6" fill="#fff"/><path d="M15 10v5M6 15h18M6 15v5M15 15v5M24 15v5" stroke="#fff" stroke-width="2"/><rect x="2" y="20" width="7" height="6" fill="#fff"/><rect x="12" y="20" width="7" height="6" fill="#fff"/><rect x="21" y="20" width="7" height="6" fill="#fff"/></svg>
    Project Management
  </div>
  <div class="abs service-btn" style="top:393px;height:58px">
    <svg viewBox="0 0 30 30"><circle cx="15" cy="11" r="8" stroke="#fff" stroke-width="2.5" fill="none"/><path d="M12 20h6M12 23h6M13 26h4" stroke="#fff" stroke-width="2"/></svg>
    Professional Consulting<br>Services
  </div>
  <div class="abs hero-caption">Dedication to Customers and IT Excellence</div>
</section>

<section>
  <div class="abs wwd-band"></div>
  <h2 class="abs wwd-title">WHAT WE DO</h2>
  <div class="abs wwd-body"></div>

  <div class="abs cluster-icon" style="left:216px"><span>
    <svg width="44" height="44" viewBox="0 0 30 30"><path d="M6 14a9 9 0 0 1 16-5M24 16a9 9 0 0 1-16 5" stroke="#fff" stroke-width="2" fill="none"/><path d="M19 5l5 4-6 2zM11 25l-5-4 6-2z" fill="#fff"/></svg></span></div>
  <div class="abs cluster-icon" style="left:419px"><span>
    <svg width="42" height="42" viewBox="0 0 30 30"><rect x="12" y="4" width="7" height="6" fill="#fff"/><path d="M15 10v5M6 15h18M6 15v5M15 15v5M24 15v5" stroke="#fff" stroke-width="2"/><rect x="2" y="20" width="7" height="6" fill="#fff"/><rect x="12" y="20" width="7" height="6" fill="#fff"/><rect x="21" y="20" width="7" height="6" fill="#fff"/></svg></span></div>
  <div class="abs cluster-icon" style="left:618px"><span>
    <svg width="40" height="40" viewBox="0 0 30 30"><circle cx="15" cy="11" r="8" stroke="#fff" stroke-width="2" fill="none"/><path d="M12 20h6M12 23h6M13 26h4" stroke="#fff" stroke-width="2"/></svg></span></div>
  <div class="abs cluster-icon" style="left:808px"><span>
    <svg width="44" height="44" viewBox="0 0 30 30"><circle cx="15" cy="15" r="12" stroke="#fff" stroke-width="2.5" fill="none"/><path d="M9 21l4-10 8-2-4 8z" fill="#fff"/></svg></span></div>

  <h3 class="abs cluster-title" style="left:165px">Strategy<br>Development</h3>
  <h3 class="abs cluster-title" style="left:364px">Project<br>Management</h3>
  <h3 class="abs cluster-title" style="left:560px">Professional<br>Consulting Services</h3>
  <h3 class="abs cluster-title" style="left:758px">Process Consulting<br>and Optimization</h3>

  <ul class="abs cluster-list" style="left:190px;width:165px">
    <li>IT-Strategy</li><li>IT-Architecture</li><li>IT-Development Plan</li>
  </ul>
  <ul class="abs cluster-list" style="left:373px;width:186px">
    <li>Project Portfolio Management</li><li>Program Management</li><li>Project Management</li><li>Project Controlling</li>
  </ul>
  <ul class="abs cluster-list" style="left:577px;width:176px">
    <li>Bank expert advice in the field of credit, securities business</li>
    <li>Banking Supervisory Law, liquidity management</li>
    <li>Requirement management inclusive Setup of valuation and prioritization methods</li>
  </ul>
  <ul class="abs cluster-list" style="left:764px;width:190px">
    <li>Process consulting and optimization</li>
    <li>Process analysis, process design, process documentation</li>
    <li>Process optimization on basis of established measurement methods</li>
  </ul>

  <div class="abs col-divider" style="left:365px"></div>
  <div class="abs col-divider" style="left:561px"></div>
  <div class="abs col-divider" style="left:757px"></div>
</section>

<section>
  <div class="abs about"></div>
  <h2 class="abs section-title" style="left:190px;top:893px">WHO WE ARE</h2>
  <div class="abs about-text">
    <p>Lorem ipsum dolor sit amet, consectetuer adipiscing elit, sed diam nonummy nibh euismod tincidunt ut laoreet dolore magna aliquam erat volutpat.</p>
    <p style="margin-top:17.6px">Ut wisi enim ad minim veniam, quis nostrud exerci tation ullamcorper suscipit lob&shy;ortis nisl ut aliquip ex ea commodo consequat.</p>
  </div>
  <div class="abs v-divider"></div>
  <h2 class="abs section-title" style="left:678px;top:893px">TESTIMONIALS</h2>
  <div class="abs quote-mark" style="left:676px;top:927px">“</div>
  <blockquote class="abs testimonial" style="left:682px;top:937px;width:244px">
    Lorem ipsum dolor sit amet, consec&shy;tetuer adipiscing elit, sed diam nonummy nibh euismod tincidunt ut laoreet dolore magna aliquam erat volutpat.
    <cite>Mara Olsen, Brightleaf Studio</cite>
  </blockquote>
  <div class="abs quote-mark" style="left:912px;top:998px">”</div>
</section>

<footer>
  <div class="abs site-footer"></div>
  <div class="abs footer-logo"><i></i>LOTSENWERK</div>
  <a class="abs footer-nav" style="left:403px">Company</a>
  <a class="abs footer-nav" style="left:469px">Consulting Service</a>
  <a class="abs footer-nav" style="left:587px">Partner Companies</a>
  <a class="abs footer-nav" style="left:704px">Contact</a>
  <div class="abs copyright">Copyright 2014. All rights reserved.</div>
  <span class="abs social" style="left:807px"></span>
  <span class="abs social" style="left:834px"></span>
  <span class="abs social" style="left:860px"></span>
  <span class="abs social" style="left:888px"></span>
  <span class="abs social" style="left:915px"></span>
</footer>

</body>
</html>
```